Verin Court Nine Flash website

we need a website to cater to 2 aspect of the business. We have Verin court residence and verin court office. For the office, we will get their inquire and arrange a face to face meetup to show them the office area for rent. For the residence side, it will need to be like lodgly or staymira.com. we want to allow them to book online for the date they need. We have a total of 10 different room configurations starting at $70 per night and up depending on the size of the room. example of the design is https://pelvandale.com/

Target Market(s)

the website should have detail information on the layout, designs, and luxury of the building.

Industry/Entity Type

office and service appartment rental/lease

Coding

Coded - Design and coding required

Number of Pages Required

5+ page

Requirements
Must have
• a luxury perspective
Nice to have
• example https://pelvandale.com/

```html
<!DOCTYPE html>
<html lang="en">
<head>
<meta charset="utf-8">
<title>Verin Court Nine</title>
<link rel="stylesheet" href="https://fonts.googleapis.com/css2?family=Cinzel:wght@400;600;700&family=Poppins:wght@400;500;600&display=swap">
<style>
:root{
  --gold:#d4a03c;
  --gold-dark:#c9922a;
  --gold-deep:#c48f2c;
  --ink:#1d1d1d;
  --muted:#8a8a8a;
  --page:#f3f3f3;
  --white:#ffffff;
  --footer:#121110;
}
*{box-sizing:border-box;margin:0;padding:0}
html,body{width:1200px;height:3742px;overflow:hidden}
body{position:relative;background:var(--page);font-family:"Poppins",sans-serif;color:var(--ink)}
.abs{position:absolute}
.btn-solid{position:absolute;background:var(--gold);color:var(--white);font-family:"Cinzel",serif;font-size:21px;display:flex;align-items:center;justify-content:center;letter-spacing:.5px}
.btn-line{position:absolute;border:2px solid currentColor;font-family:"Cinzel",serif;display:flex;align-items:center;justify-content:center;letter-spacing:.5px}

/* header */
.site-header{position:absolute;left:0;top:0;width:1200px;height:134px;background:var(--white)}
.brand{left:128px;top:93px;font-family:"Cinzel",serif;font-size:19px;color:var(--gold);display:flex;align-items:center;gap:8px;white-space:nowrap}
.brand-mark{width:12px;height:12px;background:var(--gold)}
.call{left:737px;top:36px;font-family:"Cinzel",serif;font-size:16px;color:var(--gold);display:flex;align-items:center;gap:8px}
.header-book{left:937px;top:26px;width:134px;height:41px;color:var(--gold);font-size:16px}
.main-nav{left:397px;top:96px;font-family:"Cinzel",serif;font-size:16px;color:var(--ink)}
.main-nav span{position:absolute;white-space:nowrap}
.main-nav .active{color:var(--gold)}

/* hero */
.hero-title{left:128px;top:292px;font-family:"Cinzel",serif;font-size:56px;line-height:58px;color:var(--ink);font-weight:600}
.hero-btn{left:128px;top:439px;width:173px;height:55px}

/* rooms */
.section-title{font-family:"Cinzel",serif;font-size:40px;white-space:nowrap;font-weight:400}
.section-title .accent{color:var(--gold)}
.rooms-title{left:0;width:1200px;top:875px;text-align:center}
.room-card{position:absolute;top:963px;width:291px;height:397px;background:var(--white)}
.room-photo{width:291px;height:186px}
.room-meta{position:absolute;left:24px;top:201px;font-size:13px;color:var(--muted);word-spacing:2px}
.room-meta span+span{margin-left:24px}
.room-name{position:absolute;left:22px;top:234px;font-size:19px;font-weight:500}
.room-desc{position:absolute;left:22px;top:271px;width:240px;font-size:13px;line-height:17px;color:var(--muted)}
.room-book{left:23px;top:328px;width:117px;height:46px;color:var(--gold);font-family:"Poppins",sans-serif;font-size:15px;font-weight:500}
.room-price{position:absolute;left:158px;top:336px;font-size:22px;font-weight:600;color:var(--gold)}
.room-price small{font-size:14px;font-weight:400;color:var(--ink)}
.slider-arrow{top:1057px}

/* about */
.about{left:0;top:1482px;width:1200px;height:545px;background:linear-gradient(100deg,var(--gold) 0%,#d8a646 45%,var(--gold-deep) 100%);overflow:hidden}
.about-shade{left:840px;top:0;width:360px;height:545px;background:linear-gradient(180deg,rgba(255,255,255,.06),rgba(150,100,20,.12))}
.about-brand{left:120px;top:235px;width:400px;display:flex;flex-direction:column;align-items:center;gap:22px;font-family:"Cinzel",serif;font-size:38px;color:var(--white);white-space:nowrap}
.about-brand-mark{width:26px;height:26px;background:var(--white)}
.about-title{left:574px;top:116px;font-family:"Cinzel",serif;font-size:40px;line-height:38px;color:var(--white);font-weight:400}
.about-text{left:572px;top:208px;width:490px;font-size:15px;line-height:23.2px;color:var(--white)}
.about-btn{left:572px;top:370px;width:173px;height:54px;color:var(--white);font-size:21px}

/* office */
.office-title{left:128px;top:2166px}
.office-text{left:128px;top:2232px;width:510px;font-size:15.5px;line-height:23.2px;color:#333}
.office-btn{left:128px;top:2412px;width:173px;height:54px}
.office-photo-a{left:128px;top:2537px;width:471px;height:300px}
.office-frame{left:676px;top:2162px;width:377px;height:543px;border:1.5px solid var(--gold-dark);border-top:none;border-right:none}
.office-photo-b{left:692px;top:2144px;width:379px;height:544px}

/* cta */
.cta{left:0;top:2997px;width:1200px;height:420px;background:linear-gradient(110deg,#d6a441,var(--gold) 50%,var(--gold-deep));}
.cta-title{left:0;top:106px;width:1200px;text-align:center;font-family:"Cinzel",serif;font-size:36px;color:var(--white);font-weight:400}
.cta-btn{left:497px;top:177px;width:206px;height:54px;color:var(--white);font-size:21px}

/* footer */
.footer-col-title{font-family:"Cinzel",serif;font-size:22px;color:var(--gold)}
.footer-text{font-size:15px;line-height:24.5px;color:var(--white)}
.footer-brand{left:0;width:1200px;top:3533px;text-align:center;font-family:"Cinzel",serif;font-size:37px;color:var(--gold)}
.footer-mark{left:588px;top:3462px;width:24px;height:24px;background:var(--gold)}
.contact-row{display:flex;gap:10px;align-items:flex-start;font-size:15px;line-height:18px;color:var(--white)}
.copyright{left:0;width:1200px;top:3670px;text-align:center;font-size:15px;color:var(--white)}
</style>
</head>
<body>

<header class="site-header">
  <div class="abs brand"><span class="brand-mark"></span>Verin Court Nine</div>
  <div class="abs call">
    <svg width="18" height="18" viewBox="0 0 24 24" fill="none" stroke="#d4a03c" stroke-width="1.6"><path d="M5 3h4l2 5-3 2a11 11 0 0 0 6 6l2-3 5 2v4a2 2 0 0 1-2 2A18 18 0 0 1 3 5a2 2 0 0 1 2-2z"/></svg>
    Call: 555 0142 876
  </div>
  <div class="btn-line header-book">Book Now</div>
  <nav class="abs main-nav">
    <span class="active" style="left:0">Home</span>
    <span style="left:94px">About</span>
    <span style="left:199px">VC Office</span>
    <span style="left:326px">VC Residence</span>
    <span style="left:491px">Media</span>
    <span style="left:592px">Contact</span>
  </nav>
</header>

<svg class="abs" style="left:0;top:134px" width="1200" height="680" viewBox="0 0 1200 680">
  <defs>
    <linearGradient id="skyGrey" x1="0" y1="0" x2="0" y2="1">
      <stop offset="0" stop-color="#d2d2d2"/><stop offset=".45" stop-color="#c3c3c3"/><stop offset=".75" stop-color="#8d8d8d"/><stop offset="1" stop-color="#4a4a4a"/>
    </linearGradient>
    <linearGradient id="towerShade" x1="0" y1="0" x2="1" y2="0">
      <stop offset="0" stop-color="#000" stop-opacity="0"/><stop offset=".55" stop-color="#000" stop-opacity="0"/><stop offset=".85" stop-color="#2a2a2a" stop-opacity=".35"/><stop offset="1" stop-color="#2a2a2a" stop-opacity=".25"/>
    </linearGradient>
  </defs>
  <g role="img" aria-label="Black and white photo of a city skyline with tall residential and office towers">
    <polygon points="0,0 1200,0 1200,536 600,666 0,536" fill="url(#skyGrey)"/>
    <polygon points="0,0 1200,0 1200,536 600,666 0,536" fill="url(#towerShade)"/>
  </g>
  <path d="M40,546 L600,658 L1160,546 L600,666 Z" fill="#ffffff"/>
  <path d="M30,552 L600,672 L1170,552 L600,660 Z" fill="#d39a2e"/>
</svg>
<div class="abs hero-title">Welcome to<br>Verin Court Nine</div>
<div class="btn-solid hero-btn">Read More</div>

<h2 class="abs section-title rooms-title"><span class="accent">Our Residences</span> Rooms</h2>

<svg class="abs slider-arrow" style="left:42px" width="44" height="44" viewBox="0 0 44 44" fill="none" stroke="#8a8a8a" stroke-width="1.6"><circle cx="22" cy="22" r="20"/><path d="M25 13l-9 9 9 9"/></svg>
<svg class="abs slider-arrow" style="left:1116px" width="44" height="44" viewBox="0 0 44 44" fill="none" stroke="#8a8a8a" stroke-width="1.6"><circle cx="22" cy="22" r="20"/><path d="M19 13l9 9-9 9"/></svg>

<article class="room-card" style="left:128px">
  <div class="room-photo" role="img" aria-label="Photo of a one bed room with warm wood panelling" style="background:linear-gradient(90deg,#a98563,#e9e3da 30%,#ede8e1 70%,#b0906d),linear-gradient(180deg,transparent,#c9b39a)"></div>
  <div class="room-meta"><span>R No: F1201</span><span>R Size: 47.00</span></div>
  <div class="room-name">Type C, One Bed Room</div>
  <p class="room-desc">Lorem ipsum dolor sit ametlore con sectetur adipilorescin.</p>
  <div class="btn-line room-book">Book Now</div>
  <div class="room-price">$70 <small>/night</small></div>
</article>
<article class="room-card" style="left:455px">
  <div class="room-photo" role="img" aria-label="Photo of a studio living area with a grey sofa" style="background:linear-gradient(180deg,#8f857a,#cfc8bd 45%,#e2ddd5 70%,#b7aea2)"></div>
  <div class="room-meta"><span>R No: F1202</span><span>R Size: 36.80</span></div>
  <div class="room-name">Type A, Studio</div>
  <p class="room-desc">Lorem ipsum dolor sit ametlore con sectetur adipilorescin.</p>
  <div class="btn-line room-book">Book Now</div>
  <div class="room-price">$70 <small>/night</small></div>
</article>
<article class="room-card" style="left:780px">
  <div class="room-photo" role="img" aria-label="Photo of a bright white studio lounge" style="background:linear-gradient(180deg,#f1eeea,#e6dfd6 55%,#d7bd9f 85%,#cfb08e)"></div>
  <div class="room-meta"><span>R No: F1203</span><span>R Size: 38.75</span></div>
  <div class="room-name">Type B, Studio</div>
  <p class="room-desc">Lorem ipsum dolor sit ametlore con sectetur adipilorescin.</p>
  <div class="btn-line room-book">Book Now</div>
  <div class="room-price">$70 <small>/night</small></div>
</article>

<section class="abs about">
  <div class="abs about-shade"></div>
  <div class="abs about-brand"><span class="about-brand-mark"></span>Verin Court Nine</div>
  <h2 class="abs about-title">About<br>Verin Court Nine</h2>
  <p class="abs about-text">Lorem ipsum dolor sit amet, consectetur adipiscing elit, sed do eiusmod tempor incididunt ut labore et dolore magna aliquauis ipsum suspendisse ultrices gravida. Risus commodo viverra maecenas accumsan lacus vel facilisis. Lorem ipsum dolor sit consectetur adipiscing elit, sed do eiusmod tempor incidi dunt ut labore et dolore magna aliquauis ipsum.</p>
  <div class="btn-line about-btn">Read More</div>
</section>

<h2 class="abs section-title office-title"><span class="accent">Verin Court</span> Office</h2>
<p class="abs office-text">Lorem ipsum dolor sit amet, consectetur adipiscing elit, sed do eiusmod tempor incididunt ut labore et dolore magna aliquauis ipsum suspendisse ultrices gravida. Risus commodo viverra maecenas accumsan lacus vel facilisis. Lorem ipsum dolor sit amet, consectetur adipiscing elit, sed do eiusmod tempor incidi dunt ut labore et dolore magna aliquauis ipsum.e ultrices gravida. Risus commodo viverra maecenas accumsan lacu.</p>
<div class="btn-solid office-btn">Read More</div>
<div class="abs office-photo-a" role="img" aria-label="Photo of city towers at sunset" style="background:linear-gradient(180deg,#6f6c66 0%,#a59a86 20%,#d2ad6c 42%,#8c7650 58%,#403b33 78%,#23211d 100%)"></div>
<div class="abs office-frame"></div>
<div class="abs office-photo-b" role="img" aria-label="Photo looking up at a glass office tower against the sky" style="background:radial-gradient(ellipse at 50% 55%,#2f3a44 0%,#2f3a44 25%,transparent 55%),linear-gradient(180deg,#47627f,#8ea3b6 45%,#b7b3a6 65%,#2b3136 100%)"></div>

<section class="abs cta">
  <h2 class="abs cta-title">Interested In Our Property?</h2>
  <div class="btn-line cta-btn">Register Now</div>
</section>

<svg class="abs" style="left:0;top:3280px" width="1200" height="462" viewBox="0 0 1200 462">
  <path d="M0,137 L600,12 L1200,137 L1200,462 L0,462 Z" fill="#f4e1b8"/>
  <path d="M0,150 L600,20 L1200,150 L1200,462 L0,462 Z" fill="#ffffff"/>
  <path d="M0,160 L600,32 L1200,160 L1200,462 L0,462 Z" fill="#121110"/>
</svg>

<footer>
  <div class="abs footer-col-title" style="left:130px;top:3432px">About</div>
  <p class="abs footer-text" style="left:127px;top:3478px;width:270px">Lorem ipsum dolor sit amet, consectetur adipiscing elit, sed do eiusmod tempor incididunt ut labore et dolore magna aliqua. Quis ipsum suspendisse.</p>

  <div class="abs footer-mark"></div>
  <div class="abs footer-brand">Verin Court Nine</div>
  <svg class="abs" style="left:530px;top:3603px" width="140" height="44" viewBox="0 0 140 44" fill="none" stroke="#6a6154" stroke-width="1.5">
    <circle cx="22" cy="22" r="19"/><circle cx="71" cy="22" r="19"/><circle cx="119" cy="22" r="19"/>
  </svg>

  <div class="abs footer-col-title" style="left:825px;top:3432px">Head Office</div>
  <div class="abs contact-row" style="left:827px;top:3472px">
    <svg width="15" height="15" viewBox="0 0 24 24" fill="#d4a03c"><path d="M5 2h4l2 6-3 2a12 12 0 0 0 6 6l2-3 6 2v4a2 2 0 0 1-2 2A19 19 0 0 1 3 4a2 2 0 0 1 2-2z"/></svg>
    +61-3-5550-1420
  </div>
  <div class="abs contact-row" style="left:827px;top:3512px">
    <svg width="15" height="15" viewBox="0 0 24 24" fill="#d4a03c"><path d="M2 5h20v14H2z"/><path d="M2 5l10 8 10-8" stroke="#121110" stroke-width="2" fill="none"/></svg>
    projects@verincourtnine.com
  </div>
  <div class="abs contact-row" style="left:827px;top:3550px">
    <svg width="15" height="17" viewBox="0 0 24 28" fill="#d4a03c"><path d="M12 0a10 10 0 0 1 10 10c0 7-10 18-10 18S2 17 2 10A10 10 0 0 1 12 0zm0 6a4 4 0 1 0 0 8 4 4 0 0 0 0-8z"/></svg>
    <span>42 Halden Row  VCN 3091<br>Dummy Lorem ipsum</span>
  </div>

  <div class="abs copyright">2024 © Copyright. All Rights are Reserved. Privacy Policy | imprint</div>
</footer>

</body>
</html>
```